Lena Corvel Business Card

I need a business card that reflects my current website: itslenacorvel.com and screenshot attached. If we keep the color scheme of the site and sample card below that would be ideal. The business card should include the information on the attached sample cards.

Industry/Entity Type

Business

```html
<!DOCTYPE html>
<html lang="en">
<head>
<meta charset="utf-8">
<title>Lena Corvel Business Card</title>
<link href="https://fonts.googleapis.com/css2?family=Open+Sans:ital,wght@0,400;1,400&display=swap" rel="stylesheet">
<style>
  :root {
    --stage: #d9d9d9;
    --card-black: #111213;
    --card-teal: #5cc2b0;
    --ink-white: #ffffff;
    --photo-light: #8fa9c4;
    --photo-mid: #5f7a99;
    --photo-dark: #3b4f68;
  }
  * { box-sizing: border-box; margin: 0; padding: 0; }
  html, body {
    width: 1200px;
    height: 900px;
    overflow: hidden;
    background: var(--stage);
    font-family: "Open Sans", Arial, sans-serif;
  }
  .canvas {
    position: relative;
    width: 1200px;
    height: 900px;
  }
  .card {
    position: absolute;
    left: 280px;
    width: 640px;
    height: 366px;
    overflow: hidden;
    box-shadow: 0 10px 28px rgba(0,0,0,0.28);
  }
  .card--back {
    top: 64px;
    background: var(--card-black);
  }
  .card--front {
    top: 470px;
    background: var(--card-teal);
    color: var(--ink-white);
  }
  .wordmark {
    position: absolute;
    left: 44px;
    bottom: 58px;
    color: var(--ink-white);
    font-size: 40px;
    font-weight: 400;
    letter-spacing: 0.5px;
  }
  .portrait {
    position: absolute;
    left: 0;
    bottom: 0;
    width: 250px;
    height: 310px;
    background: linear-gradient(180deg, var(--photo-light) 0%, var(--photo-mid) 55%, var(--photo-dark) 100%);
    border-radius: 120px 120px 0 0;
  }
  .details {
    position: absolute;
    right: 36px;
    top: 34px;
    text-align: right;
    line-height: 1.25;
  }
  .details__tagline {
    font-style: italic;
    font-size: 13px;
    letter-spacing: 0.4px;
    margin-bottom: 14px;
  }
  .details__name {
    font-size: 22px;
    letter-spacing: 0.8px;
    margin-bottom: 16px;
  }
  .details__email,
  .details__phone {
    font-size: 19px;
    letter-spacing: 0.5px;
  }
  .details__social {
    font-size: 19px;
    letter-spacing: 0.5px;
    margin-top: 4px;
  }
  .details__site {
    font-size: 22px;
    letter-spacing: 1.5px;
    margin-top: 26px;
    opacity: 0.85;
  }
</style>
</head>
<body>
  <main class="canvas">
    <section class="card card--back" aria-label="Card back">
      <p class="wordmark">its Lena Corvel</p>
    </section>

    <section class="card card--front" aria-label="Card front">
      <div class="portrait" role="img" aria-label="Portrait photo of Lena Corvel in a denim jacket"></div>
      <div class="details">
        <p class="details__tagline">Brand Curator | Digital Storyteller | Social Entrepreneur</p>
        <p class="details__name">LENA CORVEL</p>
        <p class="details__email">me@lenacorvel.com</p>
        <p class="details__phone">240.555.0142</p>
        <p class="details__social">[fb] | [t.] | [ig] @itslenacorvel</p>
        <p class="details__site">www.itslenacorvel.com</p>
      </div>
    </section>
  </main>
</body>
</html>
```